Business Card Design

Take existing logo/brand and develop business card for sales team.
We have two separate brands and require a business card for each.

1. VoxHarbor
2. MyNimbusLinko

Refer to our websites www.voxharbor.com.au and www.mynimbuslinko.com.au for designs currently implemented and in the marketplace.

Both cards are brands of our parent company Quorvane Systems Pty Ltd - an Australian Telecommunications company in the medium business sector. We have only business customers, no retail/residential consumers.

Target Market(s)

Australian Business - small to medium enterprise

Industry/Entity Type

Business

Contact Information for Business Card

Ted Ramsell
Sales Director
Mobile: +61 428 163 907
Direct: +61 3 9172 5836
Email: ted@voxharbor.com.au
VoxHarbor (a brand of Quorvane Systems Pty Ltd)

Ted Ramsell
Sales Director
Mobile: +61 428 163 907
Direct: +61 3 9172 5836
Email: ted@mynimbuslinko.com.au
MyNimbusLinko (a brand of Quorvane Systems Pty Ltd)

Font styles to use
Sans Serif
Other font styles liked:
• Roboto Condensed, Open Sans

Requirements
Must have
• Clean lines, crisp fonts - suggest Roboto Condensed or similar.
• Must be easy to read and clear.
• Brand colour #0C8CCD
• Two colour maximum
Nice to have
• Modern, intellectual and unique design.
Should not have
• No die cuts
• No copies or rip-offs of other designs

```html
<!DOCTYPE html>
<html lang="en">
<head>
<meta charset="utf-8">
<title>VoxHarbor Business Card</title>
<link rel="stylesheet" href="https://fonts.googleapis.com/css2?family=Open+Sans:wght@400;700&family=PT+Sans:wght@400;700&display=swap">
<style>
  :root {
    --brand-blue: #0c8ccd;
    --ink: #333333;
    --charcoal: #3a3a3c;
    --paper: #ffffff;
    --backdrop: #d9d9d9;
    --card-shadow: rgba(0, 0, 0, 0.18);
  }
  * { margin: 0; padding: 0; box-sizing: border-box; }
  html, body {
    width: 1200px;
    height: 1200px;
    overflow: hidden;
    background: var(--backdrop);
  }
  .canvas {
    width: 1200px;
    height: 1200px;
    display: flex;
    flex-direction: column;
    align-items: center;
    justify-content: center;
    gap: 64px;
  }
  .card {
    position: relative;
    width: 720px;
    height: 440px;
    overflow: hidden;
    box-shadow: 0 10px 30px var(--card-shadow);
  }
  .card--front { background: var(--paper); color: var(--ink); }
  .card--back { background: var(--charcoal); }

  .brand {
    display: flex;
    align-items: center;
    gap: 24px;
    font-family: "Open Sans", sans-serif;
    font-weight: 400;
    color: var(--brand-blue);
    letter-spacing: -1px;
    line-height: 1;
    white-space: nowrap;
  }
  .brand__dot {
    border-radius: 50%;
    background: var(--brand-blue);
    flex-shrink: 0;
  }

  .card--front .brand {
    position: absolute;
    left: 48px;
    top: 44px;
    font-size: 88px;
  }
  .card--front .brand__dot { width: 120px; height: 120px; }

  .parent-line {
    position: absolute;
    right: 44px;
    top: 178px;
    font-family: "PT Sans", sans-serif;
    font-size: 17px;
    color: var(--ink);
  }

  .person {
    position: absolute;
    left: 48px;
    top: 248px;
    font-family: "PT Sans", sans-serif;
  }
  .person__name { font-size: 40px; font-weight: 400; line-height: 1.1; }
  .person__role { font-size: 22px; margin-top: 4px; }

  .divider {
    position: absolute;
    left: 360px;
    top: 252px;
    width: 4px;
    height: 96px;
    background: var(--brand-blue);
  }

  .contact {
    position: absolute;
    left: 400px;
    top: 262px;
    font-family: "PT Sans", sans-serif;
    font-size: 19px;
    line-height: 1.35;
    border-collapse: collapse;
  }
  .contact th {
    text-align: left;
    font-weight: 700;
    padding-right: 22px;
  }
  .contact td { font-weight: 400; }

  .card--back .brand {
    position: absolute;
    left: 64px;
    top: 150px;
    font-size: 84px;
  }
  .card--back .brand__dot { width: 112px; height: 112px; }

  .web {
    position: absolute;
    right: 48px;
    bottom: 40px;
    font-family: "PT Sans", sans-serif;
    font-weight: 700;
    font-size: 20px;
    color: var(--brand-blue);
  }
</style>
</head>
<body>
<main class="canvas">
  <section class="card card--front">
    <div class="brand"><span class="brand__dot"></span><span class="brand__name">VoxHarbor</span></div>
    <p class="parent-line">a brand of Quorvane Systems Pty Ltd</p>
    <div class="person">
      <p class="person__name">Ted Ramsell</p>
      <p class="person__role">Sales Director</p>
    </div>
    <div class="divider"></div>
    <table class="contact">
      <tr><th>Mobile:</th><td>+61 428 163 907</td></tr>
      <tr><th>Direct:</th><td>+61 3 9172 5836</td></tr>
      <tr><th>Email:</th><td>ted@voxharbor.com.au</td></tr>
    </table>
  </section>

  <section class="card card--back">
    <div class="brand"><span class="brand__dot"></span><span class="brand__name">VoxHarbor</span></div>
    <p class="web">www.voxharbor.com.au</p>
  </section>
</main>
</body>
</html>
```